Builder Designer Lighting Package Email

We want to send out a cold call email to smaller builders in Calgary and Area that has links to our specific curated designer lighting packages at a discount. We want the email to come across as professional, and having the same feel as our website. www.lumarenlamp.com It needs to make note of Free delivery for calgary and area on purchases over $100.00 and Brevo Lighting offer installation of the lighting fixtures, Customers can contact the sales person who emailed them for more details and pricing on installation. The email body needs to have a section that can be edited to include a specific coupon code for an additional 10% off based on the sales person sending the email. Designer Lighting packages are as follows
Black Package 1
https://www.brevolamp.com/-black-pkg-1
Gold Package 1
https://www.brevolamp.com/-gold-pkg-1
Chrome Package 1
https://www.brevolamp.com/-chrome-pkg-1
Silver Package 1
https://www.brevolamp.com/-silver-pkg-1
Black Package 2
https://www.brevolamp.com/-black-pkg-2
Gold Package 2
https://www.brevolamp.com/-gold-pkg-2
Chrome Package 2
https://www.brevolamp.com/-chrome-pkg-2
Silver Package 2
https://www.brevolamp.com/-silver-pkg-2

```html
<!DOCTYPE html>
<html lang="en">
<head>
<meta charset="utf-8">
<title>Lumaren Lighting – Breeze into Spring Sale</title>
<link rel="stylesheet" href="https://fonts.googleapis.com/css2?family=Poppins:wght@300;400;500;600;700&family=Oswald:wght@500&family=Abril+Fatface&display=swap">
<style>
:root{
  --page:#f4f4f4;
  --white:#ffffff;
  --ink:#222222;
  --ink-soft:#444444;
  --red:#e0261b;
  --red-deep:#b8140c;
  --red-bright:#f2442f;
  --yellow:#fdc41b;
  --yellow-text:#f5c518;
  --magenta:#c0169c;
  --charcoal:#2e2e34;
  --black:#000000;
  --tile-line:#eeeeee;
  --link-blue:#3b67c4;
  --link-pink:#c0169c;
  --placeholder-a:#f3f3f3;
  --placeholder-b:#d9d9d9;
  --social:#5a5a62;
}
*{box-sizing:border-box;margin:0;padding:0}
html,body{width:1200px;height:3578px;overflow:hidden}
body{background:var(--page);font-family:'Poppins',sans-serif;color:var(--ink);position:relative}
.email{position:absolute;left:46px;top:0;width:1108px;height:3578px}

/* header */
.header{position:absolute;left:0;top:22px;width:1108px;height:200px;background:var(--white)}
.brand{position:absolute;left:0;top:26px;width:420px;height:122px;display:flex;align-items:center;gap:16px}
.brand-dot{width:30px;height:30px;background:var(--black);flex:none}
.brand-name{font-family:'Poppins',sans-serif;font-weight:600;font-size:36px;line-height:1.1;color:var(--black)}
.call-label{position:absolute;right:43px;top:20px;font-size:30px;font-weight:500;color:var(--ink)}
.call-number{position:absolute;right:34px;top:58px;font-size:63px;font-weight:300;color:var(--red);letter-spacing:1px}

/* hero */
.hero{position:absolute;left:0;top:185px;width:1108px;height:1168px;
  clip-path:polygon(0 0,100% 83px,100% 100%,0 100%);
  background:
    radial-gradient(circle at 20% 70%,rgba(255,140,110,.45),transparent 30%),
    radial-gradient(circle at 80% 65%,rgba(255,130,100,.4),transparent 30%),
    radial-gradient(circle at 50% 30%,rgba(255,90,60,.25),transparent 45%),
    linear-gradient(180deg,var(--red) 0%,var(--red-bright) 55%,var(--red-deep) 100%)}
.hero-copy{position:absolute;left:0;top:0;width:100%;height:100%;text-align:center;color:var(--white)}
.hero-title{position:absolute;top:180px;width:100%;font-size:86px;font-weight:300;letter-spacing:1px}
.hero-sub{position:absolute;top:297px;width:100%;font-size:37px;font-weight:300}
.hero-number{position:absolute;top:350px;width:100%;font-family:'Abril Fatface',serif;font-size:370px;line-height:1;color:var(--white);text-shadow:8px 8px 0 var(--red-deep)}
.hero-off{position:absolute;top:715px;width:100%;font-family:'Oswald',sans-serif;font-size:58px;font-weight:500}
.hero-storewide{position:absolute;top:793px;width:100%;font-family:'Oswald',sans-serif;font-size:44px;font-weight:500}
.shop-button{position:absolute;left:308px;top:867px;width:491px;height:92px;background:var(--black);color:var(--white);
  display:flex;align-items:center;justify-content:center;font-size:30px;font-weight:600;text-decoration:none}
.hero-note{position:absolute;top:1010px;width:100%;font-size:29px;font-weight:500;line-height:37px}

/* packages */
.packages{position:absolute;left:0;top:1353px;width:1108px;height:1108px;display:grid;grid-template-columns:repeat(3,1fr);grid-template-rows:repeat(3,1fr);gap:3px;background:var(--tile-line)}
.browse-tile{background:var(--yellow);padding:62px 0 0 42px}
.browse-label{font-size:29px;font-weight:600;color:var(--ink-soft);letter-spacing:1px}
.browse-title{margin-top:18px;font-size:60px;font-weight:600;line-height:62px;color:var(--ink)}
.package{background:var(--white);position:relative;text-decoration:none;color:var(--ink)}
.package-photo{position:absolute;left:62px;top:18px;width:244px;height:256px;border-radius:6px;
  background:radial-gradient(circle at 50% 45%,var(--placeholder-a),var(--placeholder-b))}
.package-name{position:absolute;left:0;bottom:36px;width:100%;text-align:center;font-size:26px;font-weight:500;letter-spacing:.5px}

/* promo */
.promo{position:absolute;left:0;top:2465px;width:554px;height:428px;background:var(--magenta);color:var(--white);padding:28px 0 0 46px}
.promo-kicker{font-size:70px;font-weight:700;line-height:76px;letter-spacing:1px}
.promo-value{font-size:104px;font-weight:700;line-height:100px}
.promo-next{margin-top:12px;font-size:29px;font-weight:400}
.promo-code{margin-top:6px;font-size:30px;font-weight:700;letter-spacing:.5px}
.promo-terms{margin-top:20px;font-size:22px;font-weight:500;line-height:33px}
.contact-box{position:absolute;left:554px;top:2465px;width:554px;height:428px;background:var(--charcoal);color:var(--white);padding:28px 0 0 46px}
.contact-heading{font-size:70px;font-weight:700;line-height:76px;letter-spacing:1px}
.contact-phone{font-size:56px;font-weight:300;color:var(--red);line-height:60px}
.contact-heading.email-heading{margin-top:36px;font-size:66px}
.contact-email{font-size:37px;font-weight:400;color:var(--yellow-text);margin-top:0}

/* footer */
.footer{position:absolute;left:-46px;top:2935px;width:1200px;height:262px;background:var(--black);color:var(--white)}
.footer-col{position:absolute;top:50px;font-size:26px;line-height:37px}
.footer-col.find{left:85px}
.footer-col.contact{left:666px;top:78px}
.footer-label{color:var(--yellow-text);font-weight:600;margin-bottom:8px}
.footer-col b{font-weight:700}

.social{position:absolute;left:0;top:3262px;width:1108px;display:flex;justify-content:center;gap:8px}
.social a{width:92px;height:92px;border-radius:50%;background:var(--social);display:block}
.legal{position:absolute;left:0;top:3420px;width:1108px;text-align:center;font-size:26px;line-height:37px;color:var(--ink)}
.legal a{text-decoration:none;font-weight:500}
.legal .site{color:var(--link-blue)}
.legal .prefs{color:var(--link-pink)}
</style>
</head>
<body>
<main class="email">
  <header class="header">
    <div class="brand"><span class="brand-dot"></span><span class="brand-name">Lumaren Lighting &amp; Fans</span></div>
    <div class="call-label">Call Us for Details</div>
    <div class="call-number">403-555-0148</div>
  </header>

  <section class="hero" role="img" aria-label="Warm red-toned photo of a bar with hanging Edison bulb pendant lights">
    <div class="hero-copy">
      <h1 class="hero-title">Breeze into Spring Sale</h1>
      <p class="hero-sub">The perfect tiem to shop for designer lightings</p>
      <div class="hero-number">25</div>
      <div class="hero-off">% OFF</div>
      <div class="hero-storewide">STORE WIDE</div>
      <a class="shop-button" href="https://www.lumarenlamp.com">SHOP NOW</a>
      <p class="hero-note">Profesional Installation and Free Delivery for Calgary and area<br>on purchases over $100.00</p>
    </div>
  </section>

  <section class="packages">
    <div class="browse-tile">
      <div class="browse-label">BROWSE</div>
      <h2 class="browse-title">Designer<br>Lighting<br>Package</h2>
    </div>
    <a class="package" href="https://www.lumarenlamp.com/-black-pkg-1"><div class="package-photo" role="img" aria-label="Black chandelier with white glass shades"></div><div class="package-name">Black Package 1</div></a>
    <a class="package" href="https://www.lumarenlamp.com/-gold-pkg-1"><div class="package-photo" role="img" aria-label="Gold two-light wall sconce with clear glass shades"></div><div class="package-name">Gold Package 1</div></a>
    <a class="package" href="https://www.lumarenlamp.com/-chrome-pkg-1"><div class="package-photo" role="img" aria-label="Chrome square flush mount ceiling light"></div><div class="package-name">Chrome Package 1</div></a>
    <a class="package" href="https://www.lumarenlamp.com/-silver-pkg-1"><div class="package-photo" role="img" aria-label="Silver drum pendant with white shade"></div><div class="package-name">Silver Package 1</div></a>
    <a class="package" href="https://www.lumarenlamp.com/-black-pkg-2"><div class="package-photo" role="img" aria-label="Black modern chandelier with clear glass cylinders"></div><div class="package-name">Black Package 2</div></a>
    <a class="package" href="https://www.lumarenlamp.com/-gold-pkg-2"><div class="package-photo" role="img" aria-label="Gold chandelier with white glass shades"></div><div class="package-name">Gold Package 2</div></a>
    <a class="package" href="https://www.lumarenlamp.com/-chrome-pkg-2"><div class="package-photo" role="img" aria-label="Chrome orb chandelier with square white shades"></div><div class="package-name">Chrome Package 2</div></a>
    <a class="package" href="https://www.lumarenlamp.com/-silver-pkg-2"><div class="package-photo" role="img" aria-label="Silver three-light vanity bar with white shades"></div><div class="package-name">Silver Package 2</div></a>
  </section>

  <section class="promo">
    <div class="promo-kicker">ADDITIONAL</div>
    <div class="promo-value">10% OFF</div>
    <div class="promo-next">ON YOUR NEXT ORDER</div>
    <div class="promo-code">PROMO CODE: LLJUL10</div>
    <div class="promo-terms">***Offer valid until 15th August, 2020,<br>You can&nbsp; use promoe code once</div>
  </section>
  <section class="contact-box">
    <div class="contact-heading">CALL US</div>
    <div class="contact-phone">403-555-0148</div>
    <div class="contact-heading email-heading">EMAIL:</div>
    <div class="contact-email">info@lumarenlamp.com</div>
  </section>

  <footer class="footer">
    <div class="footer-col find">
      <div class="footer-label">FIND US:</div>
      LUMAREN LIGHTING AND FANS<br>2210 Marlow Crescent SE<br>Calgary, AB T2X 0K4
    </div>
    <div class="footer-col contact">
      <div class="footer-label">CONTACT US:</div>
      <b>Phone #:</b> 403-555-0148<br><b>Fax #:</b> 403-555-0172
    </div>
  </footer>

  <nav class="social" aria-label="Social links">
    <a href="#" aria-label="Social profile 1"></a>
    <a href="#" aria-label="Social profile 2"></a>
    <a href="#" aria-label="Social profile 3"></a>
  </nav>

  <p class="legal">You have received this letter because you subscribed <a class="site" href="https://www.lumarenlamp.com">https://www.lumarenlamp.com</a>.<br>For your email preference please <a class="prefs" href="#">click here</a></p>
</main>
</body>
</html>
```